Webbanner-Design für Informatik Dienstleistungen und Webdesign
Zielgruppe
Informatik Dienstleistungen und Webdesign
Aufgabenstellung
Es soll immer das gleiche Gesicht auf den Banner und ein kurzer Satz.
1. Sie haben das Business - wir die Software
2. Sie haben Anforderungen - wir Lösungen
3. Sie brauchen Unterstützung - wir helfen
Die Banner sollen auf unserer Homepage www.varmek-design.ch auf der Startseite durchlaufen. Das Format soll 1200x500 Pixel sein

```html
<!DOCTYPE html>
<html lang="de">
<head>
<meta charset="UTF-8">
<title>Sie haben das Business – wir die Software</title>
<link href="https://fonts.googleapis.com/css2?family=Roboto+Condensed:wght@300;400;700&display=swap" rel="stylesheet">
<style>
  :root {
    --navy-deep: #0a1836;
    --navy: #10264f;
    --navy-light: #1a3766;
    --accent-blue: #1f8fe0;
    --text-white: #ffffff;
    --caption-grey: #b7bfcc;
    --portrait-dark: #1b1d24;
    --portrait-hair: #7b5b3e;
    --portrait-skin: #c4957a;
  }
  * { margin: 0; padding: 0; box-sizing: border-box; }
  html, body {
    width: 1200px;
    height: 500px;
    overflow: hidden;
    background: var(--navy-deep);
  }
  .banner {
    position: relative;
    width: 1200px;
    height: 500px;
    overflow: hidden;
    font-family: "Roboto Condensed", "Arial Narrow", sans-serif;
    background:
      radial-gradient(ellipse 420px 300px at 330px 300px, var(--navy-light) 0%, transparent 70%),
      linear-gradient(90deg, var(--navy) 0%, var(--navy-deep) 55%, #0b1530 100%);
  }
  .tech-backdrop {
    position: absolute;
    left: 0; top: 0;
    width: 760px; height: 500px;
    background: radial-gradient(circle 160px at 500px 380px, rgba(60, 100, 160, 0.25) 0%, transparent 80%);
  }
  .portrait {
    position: absolute;
    right: 0; top: 0;
    width: 640px; height: 500px;
    background:
      radial-gradient(ellipse 200px 250px at 300px 270px, var(--portrait-skin) 0%, rgba(196,149,122,0.6) 55%, transparent 80%),
      radial-gradient(ellipse 300px 340px at 300px 230px, var(--portrait-hair) 0%, transparent 75%),
      linear-gradient(90deg, rgba(11,21,48,0) 0%, var(--portrait-dark) 25%, #2a2a30 100%);
    -webkit-mask-image: linear-gradient(90deg, transparent 0%, #000 18%);
            mask-image: linear-gradient(90deg, transparent 0%, #000 18%);
  }
  .headline {
    position: absolute;
    left: 78px;
    top: 156px;
    color: var(--text-white);
  }
  .headline-lead {
    display: block;
    font-weight: 300;
    font-size: 43px;
    line-height: 50px;
    letter-spacing: 0.2px;
  }
  .headline-strong {
    display: block;
    font-weight: 700;
    font-size: 60px;
    line-height: 72px;
  }
  .accent-rule {
    position: absolute;
    left: 80px;
    top: 311px;
    width: 80px;
    height: 5px;
    background: var(--accent-blue);
  }
  .pointer-arrow {
    position: absolute;
    left: 498px;
    top: 344px;
  }
  .ambassador {
    position: absolute;
    left: 438px;
    top: 392px;
    width: 146px;
    text-align: center;
    color: var(--caption-grey);
    font-size: 14px;
    line-height: 22px;
  }
  .ambassador-name { display: block; font-weight: 400; }
  .ambassador-sport { display: block; font-weight: 700; }
</style>
</head>
<body>
  <div class="banner">
    <div class="tech-backdrop" role="img" aria-label="Dezenter technischer Hintergrund mit Schaltkreismustern in Dunkelblau"></div>
    <div class="portrait" role="img" aria-label="Porträtfoto einer jungen Frau mit langen braunen Haaren vor dunklem Hintergrund"></div>

    <h1 class="headline">
      <span class="headline-lead">Sie haben das Business –</span>
      <span class="headline-strong">wir die Software</span>
    </h1>
    <div class="accent-rule"></div>

    <svg class="pointer-arrow" width="50" height="42" viewBox="0 0 50 42" aria-hidden="true">
      <path d="M4 40 Q12 14 44 6" fill="none" stroke="#b7bfcc" stroke-width="1.6"/>
      <path d="M36 2 L46 5.5 L39 13" fill="none" stroke="#b7bfcc" stroke-width="1.6"/>
    </svg>

    <p class="ambassador">
      <span class="ambassador-name">Lina Forrer</span>
      <span class="ambassador-sport">Beachvolleyball</span>
    </p>
  </div>
</body>
</html>
```